real esate business card with company logo and name

we need a business card design for a real esate company

The company name is Walsh & Brody Pty Ltd, and we have our logo designed and will upload. We want classic or moden feel. Black or white background. looks more textured. Should include folowinginformations
Paul Walsh and Lucy Brody
Sales Agents & Onsite Manager
p: 07 5948 2063
F: 07 5948 2174
M:0461 857 239
3/42 Marlin Crescent, HARLOW PARK QLD 4315

We want this business card looks professonal. Thank you in advance.

Industry/Entity Type

Real Estate Agent

Contact Information for Business Card

Paul Walsh and Lucy Brody
Onsite Manager & Sales Agents
p: 07 5948 2063
M:0461 857 239

Font styles to use
Serif

Colors
000000
fbfbfb
333333
959595

Requirements
Must have
• company logo and name, black or white back ground

```html
<!DOCTYPE html>
<html lang="en">
<head>
<meta charset="utf-8">
<title>Walsh &amp; Brody Pty Ltd – Business Card</title>
<link href="https://fonts.googleapis.com/css2?family=Quicksand:wght@400;500;700&display=swap" rel="stylesheet">
<style>
  :root {
    --ink: #000000;
    --paper: #fbfbfb;
    --charcoal: #333333;
    --charcoal-deep: #262626;
    --steel: #959595;
    --steel-light: #c4c4c4;
    --steel-pale: #dcdcdc;
    --icon-badge: #8a8a8a;
    --backdrop: #e6e6e6;
    --text-light: #ececec;
    --brand-grey: #6f6f6f;
  }
  * { margin: 0; padding: 0; box-sizing: border-box; }
  html, body {
    width: 1200px; height: 800px; overflow: hidden;
    background: var(--backdrop);
    font-family: "Quicksand", sans-serif;
  }
  .canvas {
    width: 1200px; height: 800px;
    display: flex; align-items: center; justify-content: center;
  }
  .card {
    position: relative;
    width: 840px; height: 480px;
    background: var(--paper);
    box-shadow: 0 10px 30px rgba(0,0,0,0.18);
    overflow: hidden;
  }
  .card__brand {
    position: absolute; left: 0; top: 0;
    width: 360px; height: 100%;
    display: flex; align-items: center; justify-content: center; gap: 12px;
  }
  .brand__mark { width: 14px; height: 14px; background: var(--steel); }
  .brand__name {
    font-weight: 500; font-size: 21px; letter-spacing: 1px;
    color: var(--brand-grey); text-transform: uppercase;
  }
  .card__info {
    position: absolute; left: 360px; top: 0;
    width: 480px; height: 100%;
    background: linear-gradient(160deg, #363636 0%, var(--charcoal-deep) 100%);
  }
  .card__edge {
    position: absolute; left: 360px; top: 0;
    width: 110px; height: 100%;
  }
  .info__names {
    position: absolute; left: 95px; top: 48px;
    color: var(--text-light); font-size: 29px; line-height: 35px;
    font-weight: 400; text-transform: uppercase; letter-spacing: 0.5px;
  }
  .info__names strong { font-weight: 700; }
  .info__role {
    position: absolute; left: 95px; top: 122px;
    width: 340px; padding-bottom: 8px;
    color: var(--text-light); font-size: 17px; letter-spacing: 1px;
    border-bottom: 2px solid var(--steel);
  }
  .info__contact {
    position: absolute; left: 115px; top: 168px;
    color: var(--text-light); font-size: 18px; line-height: 22px;
    letter-spacing: 1.2px; font-weight: 400;
  }
  .info__divider {
    position: absolute; left: 125px; top: 262px;
    width: 240px; border-top: 1px solid var(--steel);
  }
  .info__address {
    position: absolute; left: 125px; top: 284px;
    color: var(--text-light); font-size: 18px; line-height: 22px;
    letter-spacing: 1.2px; font-weight: 400; font-style: normal;
  }
</style>
</head>
<body>
<main class="canvas">
  <article class="card">
    <section class="card__brand">
      <span class="brand__mark"></span>
      <span class="brand__name">Walsh &amp; Brody Pty Ltd.</span>
    </section>

    <section class="card__info">
      <h1 class="info__names">Paul <strong>Walsh</strong><br>&amp; Lucy <strong>Brody</strong></h1>
      <p class="info__role">Onsite Manager &amp; Sales Agents</p>
      <p class="info__contact">p: 07 5948 2063<br>F: 07 5948 2174<br>M:0461 857 239</p>
      <div class="info__divider"></div>
      <address class="info__address">3/42 Marlin Crescent,<br>HARLOW PARK QLD 4315</address>
    </section>

    <svg class="card__edge" viewBox="0 0 110 480" width="110" height="480" aria-hidden="true">
      <rect x="0" y="0" width="12" height="480" fill="var(--charcoal)"/>
      <rect x="12" y="0" width="14" height="480" fill="var(--steel)"/>
      <path d="M26 110 L46 118 L54 132 L54 240 L66 262 L66 380 L56 398 L26 398 Z" fill="var(--steel-light)"/>
      <path d="M26 120 L42 126 L48 138 L48 242 L60 264 L60 376 L52 390 L26 390 Z" fill="var(--steel-pale)"/>
      <polygon points="38,190 51,182 64,190 64,206 51,214 38,206" fill="var(--icon-badge)"/>
      <path d="M44 194 q2 -3 7 -3 q5 0 7 3 l-1.5 2.5 h-2.5 v-1.5 h-6 v1.5 h-2.5 z M45.5 198 h11 v5 h-11 z" fill="#f2f2f2"/>
      <polygon points="42,300 55,292 68,300 68,316 55,324 42,316" fill="var(--icon-badge)"/>
      <path d="M48 308 L55 302 L62 308 H60 V315 H57 V311 H53 V315 H50 V308 Z" fill="#f2f2f2"/>
    </svg>
  </article>
</main>
</body>
</html>
```